Zielgruppe
Ich bin freie Rednerin. Ich brauche nun einen Flyer für Beerdigungsunternehmen.
Aufgabenstellung
Flyer 4-seitig, quadratisch, 15x15 cm, aufgeklappt 15x30 cm
Bilder von mir lade ich hoch, es reicht aber wenn eines verwendet wird ;)
Ein neutrales Bild mit Thema Trauer kann noch vorgeschlagen werden (nicht zu pathetisch, eher ein Steg der auf einen See hinausführt oder so)
Schriftarten: MyriadPro, Satisfaction

```html
<!DOCTYPE html>
<html lang="de">
<head>
<meta charset="utf-8">
<title>Flyer Trauerrednerin – Innenseiten</title>
<link rel="stylesheet" href="https://fonts.googleapis.com/css2?family=Source+Sans+3:wght@400;600;700&display=swap">
<style>
  :root {
    --red: #c8202e;
    --text: #2b2b2b;
    --paper: #ffffff;
    --green-light: #e4eedb;
    --green-mid: #a9c48f;
    --green-deep: #5f8a4a;
    --frame-red: #e3a3a8;
  }
  * { box-sizing: border-box; margin: 0; padding: 0; }
  html, body { width: 1200px; height: 600px; overflow: hidden; background: var(--paper); }
  body { position: relative; font-family: "Source Sans 3", "Myriad Pro", sans-serif; color: var(--text); }

  .page { position: absolute; top: 0; width: 600px; height: 600px; }
  .page--left { left: 0; }
  .page--right { left: 600px; }

  .portrait-area {
    position: absolute; inset: 0;
    background:
      linear-gradient(90deg, rgba(255,255,255,0.85) 0%, rgba(255,255,255,0.55) 40%, rgba(255,255,255,0) 70%),
      radial-gradient(ellipse at 78% 60%, #3c4250 0%, #6a7060 22%, transparent 45%),
      linear-gradient(160deg, var(--green-light) 0%, var(--green-mid) 45%, var(--green-deep) 100%);
  }
  .inner-frame {
    position: absolute; left: 40px; top: 39px; width: 520px; height: 521px;
    border: 1px solid rgba(255,255,255,0.7);
  }

  .content { position: absolute; font-size: 12px; line-height: 17px; letter-spacing: 0.15px; }
  .content--left { left: 80px; top: 77px; width: 320px; }
  .content--right { left: 680px; top: 77px; width: 445px; }

  .heading { color: var(--red); font-weight: 700; font-size: 15.5px; line-height: 18px; }
  .content p { margin-bottom: 12px; }
  .content--left .heading + p, .content--right .heading + p { margin-top: 0; }
  .heading--offer { margin-top: 22px; }

  .offer-list { list-style: none; }
  .offer-list li { position: relative; padding-left: 12px; margin-bottom: 12px; }
  .offer-list li::before { content: "~"; position: absolute; left: 0; }

  .content--right .heading--ceremony { margin-top: 9px; margin-bottom: 12px; }

  .right-frame {
    position: absolute; left: 640px; top: 39px; width: 520px; height: 521px;
    border: 1px solid var(--frame-red);
  }
  .phone-badge {
    position: absolute; left: 1006px; top: 119px;
    background: var(--red); color: #fff; font-weight: 700; font-size: 14px;
    padding: 1px 6px; transform: rotate(-3deg); letter-spacing: 0.3px;
  }
</style>
</head>
<body>
  <section class="page page--left">
    <div class="portrait-area" role="img" aria-label="Porträtfoto der Rednerin in sommerlicher, grüner Natur"></div>
    <div class="inner-frame"></div>
  </section>

  <div class="content content--left">
    <h2 class="heading">Über mich</h2>
    <p>Mit Leidenschaft beschäftige ich mich mit Menschen und deren Geschichten.</p>
    <p>Als fundiert ausgebildete Rednerin mit dem Zertifikat der Rednerakademie Rheinland, kann ich Ihnen eine würdevolle und sehr persönliche Verabschiedung Ihres geliebten Menschen gestalten. Empathisch und authentisch verbinde ich mich dessen Persönlichkeit um die Einzigartigkeit seines Lebensweges darzustellen.</p>
    <h2 class="heading heading--offer">Mein Angebot</h2>
    <ul class="offer-list">
      <li>Die Leitung der gesamten<br>Abschieds-Zeremonie</li>
      <li>Ein Vorgespräch zum Ablauf<br>der Trauerfeier</li>
      <li>Die Gestaltung einer<br>persönlichen Trauerrede</li>
      <li>Die Verabschiedung am Grab</li>
      <li>Bis zur Bestattung ständige<br>Erreichbarkeit bei Rückfragen</li>
    </ul>
  </div>

  <div class="right-frame"></div>
  <div class="phone-badge">0170 – 12 34 56 7</div>

  <div class="content content--right">
    <h2 class="heading">Die Vorbereitung</h2>
    <p>Sie möchten mich kennenlernen? Ich freue mich auf Ihren Anruf, bei welchem wir vorab schon einige Eckdaten besprechen können.</p>
    <p>Oder Sie schauen sich vorab mein Imagevideo an:<br>Scannen Sie dazu den QR-Code auf der Rückseite mit Ihrem mobilen Gerät ab.</p>
    <p>Anschließend vereinbaren wir ein Treffen, das in Ihrer vertrauten Umgebung stattfindet. Gemeinsam besprechen wir den Ablauf der Zeremonie, mögliche Rituale oder weitere Wortbeiträge. Sie erzählen mir aus dem Leben Ihres Verstorbenen, wie er als Mensch war und welche Eigenschaften er hatte.</p>
    <p>Das, was Sie mir anvertrauen, werde ich in die Trauerrede einflechten. Dabei stehen Ihre Wünsche an oberster Stelle!</p>
    <h2 class="heading heading--ceremony">Die Verabschiedungszeremonie</h2>
    <p>Die Beerdigung wird für Sie ein schwerer Tag sein. Ich werde die Zeremonie so gestalten, dass dieser Tag nicht noch schwerer für Sie wird. Ich möchte Ihnen zur Seite stehen, und Ihnen den Rücken stärken.</p>
    <p>Aus Ihren Informationen verfasse ich eine ganz persönliche Trauerrede, welche den Verstorbenen nochmal ganz intensiv in unsere Erinnerung ruft. Dabei feiern wir vor allem das Leben Ihres Angehörigen. Wir wollen dankbar zurückschauen und die schönen Momente vor Augen führen. Dabei verzichte ich auf jeden Pathos und eine aufgesetzte Sprechweisen. Es ist das letzte, was öffentlich über diesen Menschen gesagt wird. Mir ist sehr bewusst, dass dies mit größter Behutsamkeit und Wertschätzung geschehen muss.</p>
  </div>
</body>
</html>
```